Clean bold and classy business card front and back
Kwr can be the logo
My name Trent Holloman as owner
Phone email and address
Owner Trent Holloman
Phone 8505550147
Email ridgelineinsulate@mailnest.example
Address170 frank pais rd Havana fl 32399

Industry/Entity Type

Business

Contact Information for Business Card

Owner Trent Holloman
Phone 8505550147

Requirements
Must have
• Keystone wall render under Kwr logo
Nice to have
• Bold and clean. Maybe use Kwr as logo and name under it. Have logo on one side and info on the other side with logo also
• Put a pic up. It doesn't have to be that but something that can be used
• Try some fancy fonts also

```html
<!DOCTYPE html>
<html lang="en">
<head>
<meta charset="utf-8">
<title>Kwr business card front and back</title>
<link rel="stylesheet" href="https://fonts.googleapis.com/css2?family=Fredoka:wght@600&family=Montserrat:wght@400;500;700&display=swap">
<style>
  :root {
    --page: #ecebe8;
    --card: #ffffff;
    --brand-blue: #2a7fc0;
    --brand-orange: #ef7d1a;
    --ink: #222222;
    --photo-light: #f3f1ee;
    --photo-mid: #e4ded6;
  }
  * { margin: 0; padding: 0; box-sizing: border-box; }
  html, body { width: 1200px; height: 1000px; overflow: hidden; }
  body { background: var(--page); position: relative; font-family: "Montserrat", sans-serif; color: var(--ink); }

  .card {
    position: absolute; left: 265px; width: 665px; height: 397px;
    border-radius: 26px; background: var(--card); overflow: hidden;
    box-shadow: 0 6px 16px rgba(0,0,0,0.18);
  }
  .card--front { top: 73px; }
  .card--back { top: 533px; }

  .brand { position: absolute; left: 0; right: 0; text-align: center; }
  .brand__mark {
    display: block; font-family: "Fredoka", sans-serif; font-weight: 600;
    font-size: 104px; line-height: 1; color: var(--brand-orange);
  }
  .brand__name {
    display: block; margin-top: 14px; font-family: "Fredoka", sans-serif; font-weight: 600;
    font-size: 34px; line-height: 1; color: var(--brand-blue);
  }
  .card--front .brand { top: 42px; }
  .card--back .brand { top: 100px; z-index: 1; }

  .contact { position: absolute; top: 248px; left: 0; right: 0; text-align: center; }
  .contact__name { font-weight: 700; font-size: 20px; letter-spacing: 0.5px; line-height: 1; }
  .contact__role {
    display: flex; align-items: center; justify-content: center; gap: 8px;
    margin-top: 4px; color: var(--brand-orange); font-size: 14px; line-height: 1;
  }
  .contact__role::before, .contact__role::after {
    content: ""; width: 66px; height: 1px; background: var(--brand-orange);
  }
  .contact__line { font-size: 15px; line-height: 23px; }
  .contact__line--phone { margin-top: 12px; }
  .contact__line--address { letter-spacing: 2.4px; margin-top: 3px; font-size: 15px; }

  .back-photo {
    position: absolute; inset: 0;
    background: radial-gradient(ellipse at 30% 45%, var(--photo-light) 0%, var(--photo-mid) 70%, #d9d1c7 100%);
  }
</style>
</head>
<body>
  <section class="card card--front">
    <div class="brand">
      <span class="brand__mark">Kwr</span>
      <span class="brand__name">Keystone wall render</span>
    </div>
    <div class="contact">
      <p class="contact__name">TRENT HOLLOMAN</p>
      <p class="contact__role">Owner</p>
      <p class="contact__line contact__line--phone">8505550147</p>
      <p class="contact__line">ridgelineinsulate@mailnest.example</p>
      <p class="contact__line contact__line--address">428 dunmore ct Havana fl 32399</p>
    </div>
  </section>

  <section class="card card--back">
    <div class="back-photo" role="img" aria-label="Faded photo of an installer in protective suit spraying insulation foam between roof rafters"></div>
    <div class="brand">
      <span class="brand__mark">Kwr</span>
      <span class="brand__name">Keystone wall render</span>
    </div>
  </section>
</body>
</html>
```